Heating and Air Conditioning Company Van

This will be the first van in my fleet that I am getting wrapped. Looking to utilize the colors in the motorcycle pic and possibly add some hints of red for heating (or maybe not). I am looking for a full wrap design.

My company does heating and air conditioning with a focus on energy efficient systems. I want to convey the energy efficiency with the green and blue but also want it to look like an HVAC truck (usually red and blue), but also want to stand out from the rest of the HVAC companies.

Ive also attached a picture of a van wrap that somebody else did for me that I kind of like but don't love.

```html
<!DOCTYPE html>
<html lang="en">
<head>
<meta charset="UTF-8">
<title>Verdant Heating &amp; Air Conditioning – Van Wrap Sides</title>
<link rel="stylesheet" href="https://fonts.googleapis.com/css2?family=Rubik:wght@700;800&family=Roboto+Condensed:wght@400;700&display=swap">
<style>
  :root {
    --wrap-blue: #2438b0;
    --wrap-blue-light: #3d55c9;
    --wrap-blue-deep: #18278a;
    --wrap-green: #9be31c;
    --wrap-navy: #1c2a8c;
    --wrap-white: #ffffff;
    --wrap-silver: #e9ecef;
    --trim-dark: #24262b;
    --page-bg: #f4f5f7;
  }
  html, body {
    margin: 0;
    padding: 0;
    width: 1117px;
    height: 1200px;
    overflow: hidden;
    background: var(--page-bg);
  }
  .canvas {
    position: relative;
    width: 1117px;
    height: 1200px;
  }
  .wrap-side {
    position: absolute;
    left: 60px;
    width: 997px;
    height: 440px;
  }
  .wrap-side--driver { top: 90px; }
  .wrap-side--passenger { top: 660px; }
  .wrap-art {
    position: absolute;
    inset: 0;
    width: 997px;
    height: 440px;
  }
  .wrap-side--passenger .wrap-art { transform: scaleX(-1); }

  .tagline {
    position: absolute;
    top: 18px;
    width: 420px;
    margin: 0;
    text-align: center;
    font-family: "Rubik", sans-serif;
    font-weight: 700;
    font-size: 17px;
    line-height: 22px;
    color: var(--wrap-green);
  }
  .brand {
    position: absolute;
    top: 100px;
    display: flex;
    align-items: flex-start;
    gap: 18px;
  }
  .brand-mark {
    width: 78px;
    height: 78px;
    margin-top: 24px;
    background: var(--wrap-green);
  }
  .brand-name {
    margin: 0;
    font-family: "Rubik", sans-serif;
    font-weight: 800;
    font-size: 80px;
    line-height: 88px;
    color: var(--wrap-white);
    letter-spacing: -1px;
  }
  .brand-service {
    margin: 2px 0 0 2px;
    font-family: "Roboto Condensed", sans-serif;
    font-weight: 400;
    font-size: 34px;
    line-height: 38px;
    color: var(--wrap-white);
    letter-spacing: 0.5px;
  }
  .contact-web, .contact-phone {
    position: absolute;
    margin: 0;
    color: var(--wrap-navy);
  }
  .contact-web {
    top: 330px;
    font-family: "Rubik", sans-serif;
    font-weight: 700;
    font-size: 19px;
  }
  .contact-phone {
    top: 318px;
    font-family: "Roboto Condensed", sans-serif;
    font-weight: 700;
    font-size: 38px;
    letter-spacing: 1px;
  }

  .wrap-side--driver .tagline { left: 150px; }
  .wrap-side--driver .brand { left: 60px; }
  .wrap-side--driver .contact-web { left: 40px; }
  .wrap-side--driver .contact-phone { left: 420px; }

  .wrap-side--passenger .tagline { left: 400px; }
  .wrap-side--passenger .brand { left: 300px; }
  .wrap-side--passenger .contact-phone { left: 300px; }
  .wrap-side--passenger .contact-web { left: 560px; }
</style>
</head>
<body>
<main class="canvas">

  <section class="wrap-side wrap-side--driver" aria-label="Driver side wrap">
    <svg class="wrap-art" viewBox="0 0 997 440" aria-hidden="true">
      <defs>
        <radialGradient id="burst-driver" cx="0.44" cy="0.45" r="0.6">
          <stop offset="0" stop-color="var(--wrap-blue-light)"/>
          <stop offset="1" stop-color="var(--wrap-blue-deep)"/>
        </radialGradient>
        <clipPath id="body-driver"><rect width="997" height="440" rx="24"/></clipPath>
      </defs>
      <g clip-path="url(#body-driver)">
        <rect class="body-blue" width="997" height="440" fill="url(#burst-driver)"/>
        <path class="band-white" d="M0 278 H700 C728 278 742 290 752 310 L800 400 H0 Z" fill="var(--wrap-white)"/>
        <path class="band-rule" d="M0 300 H650 C676 300 690 310 700 328 L738 400" fill="none" stroke="var(--wrap-navy)" stroke-width="4"/>
        <path class="band-green" d="M0 304 H648 C672 304 686 313 696 330 L733 400 H0 Z" fill="var(--wrap-green)"/>
        <rect class="trim" y="400" width="997" height="40" fill="var(--trim-dark)"/>
        <path class="rocker-green" d="M250 414 H640 L648 428 H250 Z" fill="var(--wrap-green)"/>
        <path class="rocker-white" d="M650 414 H760 L768 428 H658 Z" fill="var(--wrap-white)"/>
      </g>
    </svg>
    <p class="tagline">Our Team of Qualified HAV Technicians are Ready and always available</p>
    <div class="brand">
      <span class="brand-mark"></span>
      <div>
        <h1 class="brand-name">Verdant</h1>
        <p class="brand-service">HEATING &amp; AIR CONDITIONING</p>
      </div>
    </div>
    <p class="contact-web">verdantheatingandac.com</p>
    <p class="contact-phone">555-204-7781</p>
  </section>

  <section class="wrap-side wrap-side--passenger" aria-label="Passenger side wrap">
    <svg class="wrap-art" viewBox="0 0 997 440" aria-hidden="true">
      <defs>
        <radialGradient id="burst-passenger" cx="0.35" cy="0.45" r="0.6">
          <stop offset="0" stop-color="var(--wrap-blue-light)"/>
          <stop offset="1" stop-color="var(--wrap-blue-deep)"/>
        </radialGradient>
        <clipPath id="body-passenger"><rect width="997" height="440" rx="24"/></clipPath>
      </defs>
      <g clip-path="url(#body-passenger)">
        <rect class="body-blue" width="997" height="440" fill="url(#burst-passenger)"/>
        <path class="band-white" d="M0 278 H700 C728 278 742 290 752 310 L800 400 H0 Z" fill="var(--wrap-white)"/>
        <path class="band-rule" d="M0 300 H650 C676 300 690 310 700 328 L738 400" fill="none" stroke="var(--wrap-navy)" stroke-width="4"/>
        <path class="band-green" d="M0 304 H648 C672 304 686 313 696 330 L733 400 H0 Z" fill="var(--wrap-green)"/>
        <rect class="trim" y="400" width="997" height="40" fill="var(--trim-dark)"/>
        <path class="rocker-green" d="M250 414 H640 L648 428 H250 Z" fill="var(--wrap-green)"/>
        <path class="rocker-white" d="M650 414 H760 L768 428 H658 Z" fill="var(--wrap-white)"/>
      </g>
    </svg>
    <p class="tagline">Our Team of Qualified HAV Technicians are Ready and always available</p>
    <div class="brand">
      <span class="brand-mark"></span>
      <div>
        <p class="brand-name">Verdant</p>
        <p class="brand-service">HEATING &amp; AIR CONDITIONING</p>
      </div>
    </div>
    <p class="contact-phone">555-204-7781</p>
    <p class="contact-web">verdantheatingandac.com</p>
  </section>

</main>
</body>
</html>
```